Cover for nonfiction/memoir book "Static Beneath My Skin"

We're looking for a *nonfiction* *memoir* look that is consistent with other covers in that genre.

MUST HAVE:
- It must include the BACK COVER as it will be for print as well as an ebook.
- Title: Static Beneath My Skin
- TITLE MUST BE EASILY READ AT BRINDLECART THUMBNAIL SIZE
- Author name: Dorothea Quell
- At least one of the attached photos of Dorothea
- In COLOR
- The synopsis below
- Space for an endorsement

From the author: "I am looking for a cover that is eye catching and interesting or artistic, rather than just glamorous or pretty. If you like to edit the photos please do not completely remove the wrinkle between my eyebrows as I mention this in the book. It is okay if i look non conventional and my inner Aspie shows a little. The book is a little bit girly, and it would be good for the cover to reflect that, but mildly. No bright pink and purple designs. Please feel free to zoom in or crop the photos as you think works best"

SYNOPSIS (needs to go on the back cover)

Static Beneath My Skin is an acutely honest and often highly entertaining memoir by Dorothea Quell about life with Asperger's Syndrome. The book follows Dorothea in exploring her past and takes the reader with her on her journey to receiving and accepting her diagnosis. Instead of rehashing widely available Asperger's information, Dorothea focuses on discussing the thoughts, feelings and ideas that go along with being an Aspie, giving us a rare peek into what it really feels like to be a person on the spectrum. A must read for all those who enjoy deep personal stories or have a loved one on the spectrum that they wish to understand better.

The book dimensions will be 5x8 trade paperback and 6x9 hardcover (plus 0.25 bleed margin on all sizes - for both sizes).
Here is some more information from the publisher on cover requirements:

"I've attached a sample of both a paperback and hardcover size. Note that the spine width will be different depending on the final length of the book, so it won't be exact. That said, the front and back covers, and the flaps (for the hardcover) will always be the same as shown.
For deliverables, we need the following:

a Creative Suite 6 or earlier native .PSD (Photoshop), .ID (InDesign), or .AI (Illustrator) file. Creative Cloud files cannot be used and will not be accepted.
final file must include layered objects, and cannot be one 'background' image
Final files must be in CMYK color mode, 300dpi minimum
Total Ink saturation must be no more than 240% on any part of the cover. "True" black should use the following CMYK values: 60/40/40/100.
Fonts used in creation of the cover must be either A) embedded or B) sent with the final file
Vector art is preferred for scaling purposes"

Target Market(s)

Women of all ages. People who like psychology and personal stories.
Also parents and family members who may have a loved one on the Autism spectrum.

Requirements
Nice to have
• Bright green new leaves and greenery are good but not necessary.

```html
<!DOCTYPE html>
<html lang="en">
<head>
<meta charset="utf-8">
<title>Static Beneath My Skin — Cover Spread</title>
<link rel="stylesheet" href="https://fonts.googleapis.com/css2?family=Cinzel+Decorative:wght@700&family=Cinzel:wght@400&family=Crimson+Text:wght@400&display=swap">
<style>
  :root {
    --stage: #1f1b20;
    --ink: #3a2a22;
    --spine-dark: #3b302b;
    --spine-light: #6a5d55;
    --spine-text: #f3eee6;
    --cream: #fbfbf1;
    --pale-lime: #e6f2b0;
    --lime: #a9d83a;
    --leaf: #6fb21c;
    --deep-leaf: #3f8a12;
    --paper: #ffffff;
    --scroll: #6e5b4e;
  }
  * { margin: 0; padding: 0; box-sizing: border-box; }
  html, body { width: 1200px; height: 659px; overflow: hidden; background: var(--stage); }
  .canvas { position: relative; width: 1200px; height: 659px; }
  .spread {
    position: absolute; left: 162px; top: 29px;
    width: 875px; height: 600px;
    display: flex;
  }
  .back-cover {
    position: relative; width: 412px; height: 100%;
    background: linear-gradient(180deg, var(--cream) 0%, var(--pale-lime) 40%, var(--lime) 70%, var(--leaf) 100%);
    overflow: hidden;
  }
  .back-title {
    position: absolute; top: 38px; left: 0; width: 100%;
    text-align: center;
    font-family: "Cinzel Decorative", serif; font-weight: 700;
    font-size: 44px; line-height: 52px; color: var(--ink);
  }
  .synopsis {
    position: absolute; top: 218px; left: 22px; width: 368px;
    text-align: center;
    font-family: "Crimson Text", serif; font-size: 14px; line-height: 17px;
    color: #1d1a14;
  }
  .endorsement-space {
    position: absolute; left: 149px; top: 479px; width: 110px; height: 64px;
    background: var(--paper);
  }
  .spine {
    position: relative; width: 51px; height: 100%;
    background: linear-gradient(90deg, var(--spine-light), var(--spine-dark) 60%, #2e2521);
    display: flex; flex-direction: column; align-items: center;
    padding-top: 18px;
  }
  .spine-title, .spine-author {
    writing-mode: vertical-rl;
    font-family: "Cinzel", serif; color: var(--spine-text);
    font-size: 23px; letter-spacing: 0.5px; white-space: nowrap;
  }
  .spine-author { margin-top: 32px; font-size: 21px; }
  .front-cover {
    position: relative; width: 412px; height: 100%;
    background: linear-gradient(180deg, var(--cream) 0%, #f1f6d8 30%, #d6eb8c 45%, var(--lime) 60%, var(--deep-leaf) 100%);
    overflow: hidden;
  }
  .cover-photo {
    position: absolute; left: 0; top: 236px; width: 100%; height: 364px;
  }
  .scroll-ornament { position: absolute; left: 24px; width: 364px; }
  .scroll-top { top: 16px; height: 28px; }
  .scroll-bottom { top: 222px; height: 22px; }
  .front-author {
    position: absolute; top: 48px; width: 100%; text-align: center;
    font-family: "Cinzel", serif; font-size: 23px; color: var(--ink);
  }
  .front-title {
    position: absolute; top: 76px; width: 100%; text-align: center;
    font-family: "Cinzel Decorative", serif; font-weight: 700;
    font-size: 46px; line-height: 46px; color: var(--ink);
  }
</style>
</head>
<body>
<main class="canvas">
  <section class="spread">
    <article class="back-cover">
      <h2 class="back-title">Static<br>Beneath<br>My Skin</h2>
      <p class="synopsis">Static Beneath My Skin is an acutely honest and often highly entertaining memoir by Dorothea Quell about life with Asperger's Syndrome. The book follows Dorothea in exploring her past and takes the reader with her on her journey to receiving and accepting her diagnosis. Instead of rehashing widely available Asperger's information, Dorothea focuses on discussing the thoughts, feelings and ideas that go along with being an Aspie, giving us a rare peek into what it really feels like to be a person on the spectrum. A must read for all those who enjoy deep personal stories or have a loved one on the spectrum that they wish to understand better.</p>
      <div class="endorsement-space"></div>
    </article>

    <aside class="spine">
      <span class="spine-title">Static Beneath My Skin</span>
      <span class="spine-author">Dorothea Quell</span>
    </aside>

    <article class="front-cover">
      <svg class="cover-photo" role="img" aria-label="Photo of Dorothea lying in tall green grass, smiling and writing in a notebook" viewBox="0 0 412 364" preserveAspectRatio="none">
        <defs>
          <linearGradient id="grass" x1="0" y1="0" x2="0" y2="1">
            <stop offset="0" stop-color="#b8dc5a"/>
            <stop offset="0.5" stop-color="#7cbf2a"/>
            <stop offset="1" stop-color="#3d8414"/>
          </linearGradient>
          <radialGradient id="portrait" cx="0.55" cy="0.5" r="0.5">
            <stop offset="0" stop-color="#e8c9a4"/>
            <stop offset="0.45" stop-color="#d9b56e"/>
            <stop offset="0.75" stop-color="#7f9fb4" stop-opacity="0.8"/>
            <stop offset="1" stop-color="#7cbf2a" stop-opacity="0"/>
          </radialGradient>
        </defs>
        <rect width="412" height="364" fill="url(#grass)"/>
        <ellipse cx="230" cy="200" rx="190" ry="160" fill="url(#portrait)"/>
      </svg>
      <svg class="scroll-ornament scroll-top" viewBox="0 0 364 28" preserveAspectRatio="none" aria-hidden="true">
        <path d="M10 20 Q182 -4 354 20" fill="none" stroke="var(--scroll)" stroke-width="2.5"/>
      </svg>
      <p class="front-author">Dorothea Quell</p>
      <h1 class="front-title">Static<br>Beneath<br>My Skin</h1>
      <svg class="scroll-ornament scroll-bottom" viewBox="0 0 364 22" preserveAspectRatio="none" aria-hidden="true">
        <path d="M10 6 Q182 26 354 6" fill="none" stroke="var(--scroll)" stroke-width="2.5"/>
      </svg>
    </article>
  </section>
</main>
</body>
</html>
```